Corvane Capital LLC
I need single sided standard sized Business Card [3.5" x 2"]
Fonts to be determined by designer
Professional
Derek Halloway
Chairman
Kestrel Hall Tower
418 North Larkin Avenue
Los Angeles, CA 90099
555.014.2739 X1
Acquisitions@Corvane-Capital.net
http://www.Corvane-Capital.net
We want to see what designs are out there for a cutting edge business card that shows off our 3 main goals: Intense - Expressive - Important . The business card can be vertical or horizontal, can use fonts of the designer's choice and be relatively "unique". More than just a simple black on white business card.
Use the logo and CORVANE but you do not need to use the blue background if your design does not warrant it. Financial LLC can be in any font you desire if it matches your design

```html
<!DOCTYPE html>
<html lang="en">
<head>
<meta charset="utf-8">
<title>Corvane Capital LLC – Business Card</title>
<link rel="stylesheet" href="https://fonts.googleapis.com/css2?family=Didact+Gothic&family=Open+Sans:wght@400;700&display=swap">
<style>
  :root {
    --backdrop: #e8e3db;
    --card-light: #ffffff;
    --card-dark: #141414;
    --band-dark: #111111;
    --band-light: #ffffff;
    --gold: #a9803f;
    --ink: #2b2b2b;
    --paper-text: #d8d8d8;
  }
  * { box-sizing: border-box; margin: 0; padding: 0; }
  html, body {
    width: 1200px; height: 1002px; overflow: hidden;
    background: var(--backdrop);
  }
  .sheet { position: relative; width: 1200px; height: 1002px; }
  .card {
    position: absolute; top: 60px;
    width: 505px; height: 877px;
    border-radius: 30px; overflow: hidden;
    box-shadow: 0 4px 14px rgba(0,0,0,0.18);
    font-family: "Open Sans", Arial, sans-serif;
    text-align: center;
  }
  .card--light { left: 60px; background: var(--card-light); color: var(--ink); }
  .card--dark  { left: 635px; background: var(--card-dark); color: var(--paper-text); }

  .brand { position: absolute; left: 0; right: 0; top: 66px; }
  .brand__mark {
    display: block; width: 104px; height: 104px; margin: 0 auto;
    border-radius: 50%; background: var(--gold);
  }
  .brand__name {
    margin-top: 60px;
    font-family: "Didact Gothic", "Century Gothic", sans-serif;
    font-size: 56px; letter-spacing: 4px; line-height: 1;
    color: var(--gold);
  }
  .brand__sub {
    margin-top: 14px;
    font-family: "Didact Gothic", "Century Gothic", sans-serif;
    font-size: 17px; letter-spacing: 8px;
    color: var(--gold);
  }

  .nameband {
    position: absolute; left: 0; right: 0;
    display: flex; flex-direction: column; justify-content: center;
  }
  .card--light .nameband { top: 491px; height: 76px; background: var(--band-dark); color: #fff; }
  .card--dark .nameband  { top: 513px; height: 68px; background: var(--band-light); color: #111; }
  .nameband__name { font-weight: 700; font-size: 28px; line-height: 1.1; }
  .nameband__role { font-size: 18px; line-height: 1.25; }
  .card--light .nameband__role { color: #d0d0d0; }
  .card--dark .nameband__role  { color: #555; }

  .contact {
    position: absolute; left: 0; right: 0; top: 600px;
    font-size: 19px; line-height: 32px;
  }
  .contact__gap { height: 28px; }
  .contact__web { letter-spacing: 1.5px; }
</style>
</head>
<body>
<main class="sheet">

  <section class="card card--light" aria-label="Business card, light side">
    <div class="brand">
      <span class="brand__mark" aria-hidden="true"></span>
      <div class="brand__name">CORVANE</div>
      <div class="brand__sub">CAPITAL LLC</div>
    </div>
    <div class="nameband">
      <div class="nameband__name">Derek Halloway</div>
      <div class="nameband__role">Chairman</div>
    </div>
    <div class="contact">
      <p>Kestrel Hall Tower 418</p>
      <p>North Larkin Avenue Los Angeles, CA 90099</p>
      <div class="contact__gap"></div>
      <p>Phone: 555 014 2739 Ext.1</p>
      <p>Fax: 555 017 6482</p>
      <p>Email: Acquisitions@Corvane-Capital.net</p>
      <p class="contact__web">www.Corvane-Capital.net</p>
    </div>
  </section>

  <section class="card card--dark" aria-label="Business card, dark side">
    <div class="brand">
      <span class="brand__mark" aria-hidden="true"></span>
      <div class="brand__name">CORVANE</div>
    </div>
    <div class="nameband">
      <div class="nameband__name">Derek Halloway</div>
      <div class="nameband__role">Chairman</div>
    </div>
    <div class="contact">
      <p>Kestrel Hall Tower 418</p>
      <p>North Larkin Avenue Los Angeles, CA 90099</p>
      <div class="contact__gap"></div>
      <p>Phone: 555 014 2739 Ext.1</p>
      <p>Fax: 555 017 6482</p>
      <p>Email: Acquisitions@Corvane-Capital.net</p>
      <p class="contact__web">www.Corvane-Capital.net</p>
    </div>
  </section>

</main>
</body>
</html>
```